Custom Like Page for Circleboard
Kestrel Vale Foods
Project: Custom Like Page for Circleboard
Custom Like Page for Circleboard - Health
Creative Brief
Health
Target audience will be people who go to the gym, runners, and people who are trying to lose weight or gain muscle.
1) On the top it must say "CLICK THE "LIKE" BUTTON TO PARTICIPATE IN THE KESTREL VALE FOODS SWEEPSTAKES" (with an arrow pointing to the like button) 2)Must have pictures of people working out, running, and or exercising 3) Tell people about the $500 Grand Prize, $200 Second Prize, and $100 Third Prize . . . for the most friend referrals by December 31, 2011 4) Creative and edgey 5) A small company logo on it somewhere

```html
<!DOCTYPE html>
<html lang="en">
<head>
<meta charset="utf-8">
<title>Kestrel Vale Foods – Sweepstakes Page</title>
<link rel="stylesheet" href="https://fonts.googleapis.com/css2?family=Open+Sans:wght@400;600;700&family=Anton&family=Oswald:wght@500;700&display=swap">
<style>
:root{
  --net-blue:#3b5998;
  --net-blue-dark:#29447e;
  --net-link:#3b5998;
  --net-grey:#f2f2f2;
  --net-line:#d8dfea;
  --text:#333333;
  --muted:#808080;
  --signup:#69a74e;
  --orange-1:#f79a2a;
  --orange-2:#e85d0c;
  --orange-3:#c9450a;
  --gold:#ffe24a;
  --navy:#16264a;
  --pill:#1d3466;
  --pill-edge:#6fa0e0;
  --dollar:#4f86d6;
  --white:#ffffff;
}
*{box-sizing:border-box;margin:0;padding:0}
html,body{width:1200px;height:876px;overflow:hidden;background:var(--white)}
body{position:relative;font-family:"Open Sans",Arial,sans-serif;color:var(--text);font-size:18px}
.abs{position:absolute}

/* top bar */
.topbar{left:0;top:0;width:1200px;height:82px;background:var(--net-blue);border-bottom:2px solid var(--net-blue-dark)}
.brandname{left:150px;top:18px;color:var(--white);font-weight:700;font-size:40px;letter-spacing:-1px}
.login-label{color:var(--white);font-size:13px;top:12px}
.login-field{top:30px;width:170px;height:26px;background:var(--white);border:1px solid #1d4088}
.login-note{color:#9daccb;font-size:12px;top:60px}
.login-btn{left:1010px;top:30px;width:56px;height:26px;background:#5b74a8;border:1px solid #29447e;color:var(--white);font-weight:700;font-size:13px;text-align:center;line-height:24px}

/* signup strip */
.strip{left:0;top:84px;width:1200px;height:36px;background:var(--net-grey);border-bottom:1px solid #ccc}
.signup{left:150px;top:5px;width:58px;height:26px;background:var(--signup);border:1px solid #3b6e22;color:var(--white);font-weight:700;font-size:13px;text-align:center;line-height:24px}
.strip-text{left:218px;top:9px;font-size:13px;font-weight:700;color:var(--text)}

/* left column */
.profile{left:50px;top:130px;width:196px;height:196px;border:1px solid #ccc;display:flex;flex-direction:column;align-items:center;justify-content:center;gap:10px}
.profile-dot{width:90px;height:90px;border-radius:50%;background:#2f7fd0}
.profile-name{font-weight:700;font-size:16px;color:var(--navy)}
.nav{left:50px;top:340px;width:196px;font-size:14px}
.nav li{list-style:none;height:24px;line-height:24px;padding-left:26px;position:relative;color:var(--net-link)}
.nav li::before{content:"";position:absolute;left:4px;top:6px;width:12px;height:12px;background:#9aa9c7}
.nav li.current{background:#d8dfea;font-weight:700;color:var(--text)}
.side-h{font-size:13px;font-weight:700;color:var(--text);border-top:1px solid #ddd;padding-top:6px}
.about{left:50px;top:444px;width:196px}
.about p{font-size:12px;margin-top:8px;line-height:1.4}
.likes-count{left:50px;top:512px;font-size:22px;font-weight:700}
.likes-sub{left:50px;top:540px;font-size:12px}
.likes{left:50px;top:565px;width:196px}
.likes .see{position:absolute;right:0;top:6px;font-size:12px;color:var(--net-link);font-weight:400}
.like-item{display:flex;gap:8px;align-items:center;margin-top:8px;font-size:11px;color:var(--net-link);font-weight:700;line-height:1.25}
.like-thumb{width:48px;height:40px;flex:none;background:linear-gradient(#555,#222)}

/* centre */
.page-title{left:305px;top:137px;font-size:21px;font-weight:700;color:var(--net-link)}
.like-btn{left:500px;top:140px;width:46px;height:22px;border:1px solid #999;background:#eee;font-size:12px;font-weight:700;text-align:center;line-height:20px;color:var(--text)}
.page-sub{left:305px;top:170px;font-size:12px;color:var(--muted)}
.page-sub span{color:var(--net-link)}
.create-btn{left:906px;top:144px;width:128px;height:26px;border:1px solid #999;background:#eee;font-size:12px;font-weight:700;text-align:center;line-height:24px}

/* sweepstakes panel */
.panel{left:305px;top:204px;width:415px;height:636px;border-radius:0 0 14px 14px;overflow:hidden;
  background:linear-gradient(180deg,var(--orange-1) 0%,var(--orange-2) 55%,var(--orange-3) 100%)}
.panel .arrow{position:absolute;left:190px;top:0}
.cta{position:absolute;left:0;top:28px;width:100%;text-align:center;font-family:"Oswald",Arial,sans-serif;font-weight:700;font-size:10.5px;color:var(--gold);letter-spacing:.2px}
.burst{position:absolute;left:40px;top:42px;width:335px;height:110px;background:radial-gradient(ellipse at center,#ffd58a 0%,rgba(255,190,90,.4) 50%,rgba(255,150,40,0) 75%)}
.title{position:absolute;left:0;top:52px;width:100%;text-align:center;font-family:"Anton",Impact,sans-serif;font-size:64px;line-height:74px;color:var(--white);letter-spacing:1px;text-shadow:0 3px 6px rgba(120,40,0,.5)}
.athletes{position:absolute;left:15px;top:128px;width:385px;height:230px;border-radius:6px;
  background:radial-gradient(ellipse at 50% 40%,#f2b27e 0%,#c97a4a 40%,rgba(210,90,20,0) 75%)}
.win-band{position:absolute;left:28px;top:350px;width:360px;height:40px;background:var(--navy);color:var(--white);
  font-family:"Anton",Impact,sans-serif;font-size:32px;line-height:40px;text-align:center;letter-spacing:1px}
.prizes{position:absolute;left:20px;top:400px;width:375px;display:flex;justify-content:space-between}
.prize{width:118px;text-align:center;color:var(--white)}
.prize-pill{height:50px;border-radius:10px;background:linear-gradient(#2c4b8c,var(--pill));border:2px solid var(--pill-edge);
  display:flex;align-items:center;justify-content:center;gap:6px;font-family:"Oswald",Arial,sans-serif;font-weight:700;font-size:30px}
.dollar{width:28px;height:28px;border-radius:50%;background:var(--dollar);font-size:18px;line-height:28px}
.prize-label{font-family:"Oswald",Arial,sans-serif;font-weight:500;font-size:16px;margin-top:6px}
.refer-head{position:absolute;left:20px;top:282px}
.refer{position:absolute;left:20px;top:532px;width:195px}
.refer-title{background:linear-gradient(#f4f4f4,#c9c9c9);color:#333;font-family:"Oswald",Arial,sans-serif;font-weight:700;font-size:21px;padding:3px 10px;border-radius:3px 3px 0 0}
.refer-body{background:rgba(40,30,30,.8);color:var(--white);font-size:11.5px;line-height:1.4;padding:6px 10px;font-weight:600}
.brand-mark{position:absolute;left:255px;top:520px;width:140px;display:flex;flex-direction:column;align-items:center;gap:6px}
.brand-dot{width:74px;height:74px;border-radius:50%;background:var(--white)}
.brand-name{color:var(--white);font-weight:700;font-size:12px;white-space:nowrap}

/* right column */
.similar{left:790px;top:198px;width:260px}
.similar .side-h{border-top:none;background:#eceff5;padding:5px 6px;border-top:1px solid #ccc}
.sim-item{display:flex;gap:10px;margin-top:14px;align-items:flex-start}
.sim-thumb{width:44px;height:44px;flex:none}
.sim-name{font-size:12px;font-weight:700;color:var(--net-link);line-height:1.3}
.sim-count{font-size:11px;color:var(--muted)}
.more{left:958px;top:448px;font-size:12px;color:var(--net-link)}
</style>
</head>
<body>

<header class="abs topbar">
  <div class="abs brandname">circleboard</div>
  <span class="abs login-label" style="left:730px">Email</span>
  <div class="abs login-field" style="left:730px"></div>
  <span class="abs login-note" style="left:730px">☐ Keep me logged in</span>
  <span class="abs login-label" style="left:912px">Password</span>
  <div class="abs login-field" style="left:912px;width:90px"></div>
  <span class="abs login-note" style="left:912px">Forgot your password?</span>
  <div class="abs login-btn">Log In</div>
</header>

<div class="abs strip">
  <div class="abs signup">Sign Up</div>
  <div class="abs strip-text">Circleboard helps you connect and share with the people in your life.</div>
</div>

<aside>
  <div class="abs profile">
    <div class="profile-dot"></div>
    <div class="profile-name">KESTREL VALE FOODS</div>
  </div>
  <ul class="abs nav">
    <li>Wall</li>
    <li>Info</li>
    <li class="current">LikeKestrelValeFoods</li>
    <li>Photos</li>
  </ul>
  <div class="abs about">
    <div class="side-h">About</div>
    <p>Website is under construction, HIT THE LIKE BUTTON for updates.</p>
  </div>
  <div class="abs likes-count">242</div>
  <div class="abs likes-sub">like this</div>
  <div class="abs likes">
    <div class="side-h">Likes <span class="see">See All</span></div>
    <div class="like-item"><div class="like-thumb" role="img" aria-label="Sports drink brand tile"></div>Vireo Sport</div>
    <div class="like-item"><div class="like-thumb" role="img" aria-label="Fitness gym tile"></div>Ironkeel Fitness - Coastline Training</div>
    <div class="like-item"><div class="like-thumb" role="img" aria-label="Supplement brand tile"></div>Official Torvane Nutrition</div>
    <div class="like-item"><div class="like-thumb" role="img" aria-label="Supplement brand tile"></div>QRX</div>
    <div class="like-item"><div class="like-thumb" role="img" aria-label="Apparel brand tile"></div>Ridgeback Tactical and Combat Apparel</div>
  </div>
</aside>

<main>
  <h1 class="abs page-title">Kestrel Vale Foods</h1>
  <div class="abs like-btn">Like</div>
  <div class="abs page-sub">Small Business · <span>Lanmere, Oregon</span></div>
  <div class="abs create-btn">Create a Page</div>

  <section class="abs panel">
    <svg class="arrow" width="34" height="26" viewBox="0 0 34 26" aria-hidden="true"><path d="M17 0 L34 14 H24 V26 H10 V14 H0 Z" fill="#ffffff"/></svg>
    <div class="cta">"CLICK THE "LIKE" BUTTON TO PARTICIPATE IN THE KESTREL VALE FOODS SWEEPSTAKES"</div>
    <div class="burst"></div>
    <div class="title">SWEEPSTAKES</div>
    <div class="athletes" role="img" aria-label="Three athletes working out with dumbbells"></div>
    <div class="win-band">TO WIN PRIZES</div>
    <div class="prizes">
      <div class="prize"><div class="prize-pill"><span class="dollar">$</span>500</div><div class="prize-label">Grand Prize</div></div>
      <div class="prize"><div class="prize-pill"><span class="dollar">$</span>200</div><div class="prize-label">Second Prize</div></div>
      <div class="prize"><div class="prize-pill"><span class="dollar">$</span>100</div><div class="prize-label">Third Prize</div></div>
    </div>
    <div class="refer">
      <div class="refer-title">Refer Friends</div>
      <div class="refer-body">The participants with most Circleboard friend referrals by December 31, 2011</div>
    </div>
    <div class="brand-mark">
      <div class="brand-dot"></div>
      <div class="brand-name">KESTREL VALE FOODS</div>
    </div>
  </section>
</main>

<aside class="abs similar">
  <div class="side-h">Similar Circleboard Pages</div>
  <div class="sim-item"><div class="sim-thumb" style="background:#c44" role="img" aria-label="Sign company thumbnail"></div><div><div class="sim-name">Marlow Signs / Fineline Designs, Inc.</div><div class="sim-count">1,294 people like this.</div></div></div>
  <div class="sim-item"><div class="sim-thumb" style="background:#6a4a8c" role="img" aria-label="Badge maker thumbnail"></div><div><div class="sim-name">PinwheelBadges.net</div><div class="sim-count">2,775 people like this.</div></div></div>
  <div class="sim-item"><div class="sim-thumb" style="background:#5d7a44" role="img" aria-label="Memorial home thumbnail"></div><div><div class="sim-name">Harold P. Ansel Memorial Home</div><div class="sim-count">1,057 people like this.</div></div></div>
</aside>
<div class="abs more">More ›</div>

</body>
</html>
```